Creative Business Card

Were looking for a new fresh and creative look to our Business card. Our company name is InkHollow. Be creative, Were attaching our logo and our base colors, but your free to do anything. Name, title, Phone

Industry/Entity Type

Business

```html
<!DOCTYPE html>
<html lang="en">
<head>
<meta charset="utf-8">
<title>InkHollow Business Card</title>
<link rel="stylesheet" href="https://fonts.googleapis.com/css2?family=Open+Sans:wght@400;600;800&display=swap">
<style>
  :root {
    --stage: #e9e7e3;
    --card-dark: #26282b;
    --card-light: #ffffff;
    --brand-green: #7cc242;
    --brand-blue: #1a78c2;
    --ink: #222222;
    --band: #2a2c2f;
  }
  * { margin: 0; padding: 0; box-sizing: border-box; }
  html, body {
    width: 1200px; height: 784px; overflow: hidden;
    background: var(--stage);
    font-family: "Open Sans", Arial, sans-serif;
  }
  .stage {
    position: relative; width: 1200px; height: 784px;
  }
  .card {
    position: absolute; top: 237px;
    width: 540px; height: 309px;
    border-radius: 4px; overflow: hidden;
    box-shadow: 0 8px 22px rgba(0,0,0,0.18);
  }
  .card--front {
    left: 40px;
    background: radial-gradient(ellipse at 55% 35%, #34373b 0%, var(--card-dark) 70%);
    display: flex; align-items: center; justify-content: center;
  }
  .card--back {
    left: 620px;
    background: var(--card-light);
  }
  .wordmark {
    font-weight: 800; color: var(--brand-green);
    letter-spacing: 1px; line-height: 1;
  }
  .card--front .wordmark { font-size: 64px; margin-top: -40px; }
  .card--back .wordmark {
    position: absolute; left: 40px; top: 42px; font-size: 60px;
  }
  .bottom-band { position: absolute; left: 0; top: 0; width: 540px; height: 309px; }
  .contact-block { position: absolute; left: 40px; top: 132px; }
  .contact-name {
    font-size: 20px; font-weight: 800; color: var(--brand-green); line-height: 1.1;
  }
  .contact-title { font-size: 12px; color: var(--ink); margin: 2px 0 8px 2px; }
  .contact-list { list-style: none; }
  .contact-list li {
    display: flex; align-items: center; gap: 8px;
    font-size: 14px; color: var(--ink); height: 22px;
  }
  .contact-list svg { width: 15px; height: 15px; fill: var(--brand-green); flex: none; }
</style>
</head>
<body>
<main class="stage">
  <section class="card card--front" aria-label="Business card front">
    <div class="wordmark">InkHollow</div>
  </section>

  <section class="card card--back" aria-label="Business card back">
    <svg class="bottom-band" viewBox="0 0 540 309" aria-hidden="true">
      <polygon points="0,305 540,236 540,309 0,309" fill="var(--band)"/>
      <polygon points="0,301 540,232 540,236 0,305" fill="var(--brand-blue)"/>
    </svg>
    <div class="wordmark">InkHollow</div>
    <div class="contact-block">
      <div class="contact-name">Dana Reyes</div>
      <div class="contact-title">Manager</div>
      <ul class="contact-list">
        <li>
          <svg viewBox="0 0 24 24"><path d="M6.6 10.8a15.1 15.1 0 0 0 6.6 6.6l2.2-2.2c.3-.3.7-.4 1-.2 1.1.4 2.3.6 3.6.6.6 0 1 .4 1 1V20c0 .6-.4 1-1 1C10.6 21 3 13.4 3 4c0-.6.4-1 1-1h3.5c.6 0 1 .4 1 1 0 1.3.2 2.5.6 3.6.1.3 0 .7-.2 1z"/></svg>
          (503) 555-0142
        </li>
        <li>
          <svg viewBox="0 0 24 24"><path d="M3 5h18a1 1 0 0 1 1 1v12a1 1 0 0 1-1 1H3a1 1 0 0 1-1-1V6a1 1 0 0 1 1-1zm1 2.2V17h16V7.2l-8 5.3z M4.5 7l7.5 5 7.5-5z"/></svg>
          dana@inkhollow.com
        </li>
        <li>
          <svg viewBox="0 0 24 24"><path d="M12 2a10 10 0 1 0 0 20 10 10 0 0 0 0-20zm6.9 6h-3a15 15 0 0 0-1.3-3.9A8 8 0 0 1 18.9 8zM12 4c.9 1.2 1.6 2.5 2 4h-4c.4-1.5 1.1-2.8 2-4zM4.3 14a8 8 0 0 1 0-4h3.4a16 16 0 0 0 0 4zm.8 2h3a15 15 0 0 0 1.3 3.9A8 8 0 0 1 5.1 16zm3-8h-3a8 8 0 0 1 4.3-3.9A15 15 0 0 0 8.1 8zM12 20c-.9-1.2-1.6-2.5-2-4h4c-.4 1.5-1.1 2.8-2 4zm2.3-6H9.7a14 14 0 0 1 0-4h4.6a14 14 0 0 1 0 4zm.3 5.9a15 15 0 0 0 1.3-3.9h3a8 8 0 0 1-4.3 3.9zm1.7-5.9a16 16 0 0 0 0-4h3.4a8 8 0 0 1 0 4z"/></svg>
          www.inkhollow.com
        </li>
        <li>
          <svg viewBox="0 0 24 24"><path d="M12 3 2 12h3v8h5v-6h4v6h5v-8h3z"/></svg>
          1420 Fernwood Lane, Suite D
        </li>
      </ul>
    </div>
  </section>
</main>
</body>
</html>
```